A4 Menu needed for cafe - attached design

Need an A4 menu designed for our cafe.
I have attached our catering menu - I would like the new menu to be designed in the exact same way.

I have attached the text that needs to appear on the menu

```html
<!DOCTYPE html>
<html lang="en">
<head>
<meta charset="utf-8">
<title>Corner Cup Cafe Menu</title>
<link rel="stylesheet" href="https://fonts.googleapis.com/css2?family=Arvo:wght@400;700&family=Oswald:wght@500;600&family=Arimo:wght@400&display=swap">
<style>
  :root {
    --bg: #000000;
    --ink: #ffffff;
    --gold: #f5d45a;
    --frame: #d9d9d9;
  }
  * { box-sizing: border-box; margin: 0; padding: 0; }
  html, body { width: 849px; height: 1200px; overflow: hidden; background: var(--bg); }
  .menu-page {
    position: relative; width: 849px; height: 1200px;
    background: var(--bg); color: var(--ink);
    font-family: "Arvo", Georgia, serif; font-weight: 700;
  }
  .brand {
    position: absolute; left: 0; width: 849px; top: 52px;
    display: flex; align-items: center; justify-content: center; gap: 10px;
  }
  .brand-mark { width: 18px; height: 18px; background: var(--gold); }
  .brand-name { color: var(--ink); font-size: 22px; letter-spacing: 1px; }
  .menu-word {
    position: absolute; left: 0; width: 849px; top: 118px; text-align: center;
    color: var(--gold); font-size: 14px; letter-spacing: 4px;
  }
  .section-box { position: absolute; border: 1.5px solid var(--frame); }
  .breakfast-box { left: 51px; top: 183px; width: 366px; height: 598px; }
  .light-box { left: 442px; top: 183px; width: 366px; height: 598px; }
  .lunch-box { left: 57px; top: 820px; width: 748px; height: 285px; }
  .banner { position: absolute; display: block; }
  .banner svg { position: absolute; left: 0; top: 0; }
  .banner-label {
    position: absolute; inset: 0; display: flex; align-items: center; justify-content: center;
    font-family: "Oswald", "Arial Narrow", sans-serif; font-weight: 600;
    font-size: 22px; letter-spacing: 1.5px; color: var(--ink);
  }
  .banner-breakfast { left: 148px; top: 160px; width: 195px; height: 44px; }
  .banner-light { left: 537px; top: 160px; width: 198px; height: 44px; }
  .banner-light .banner-label { font-size: 20px; letter-spacing: 0.5px; }
  .banner-lunch { left: 43px; top: 798px; width: 186px; height: 44px; }
  .banner-lunch .banner-label { justify-content: flex-start; padding-left: 62px; }
  .item-list { position: absolute; list-style: none; font-size: 15.5px; }
  .item { display: flex; justify-content: space-between; height: 41px; align-items: center; white-space: nowrap; }
  .breakfast-list { left: 78px; top: 233px; width: 320px; }
  .light-list { left: 468px; top: 233px; width: 318px; }
  .lunch-list { top: 874px; font-size: 15px; font-weight: 400; }
  .lunch-list .item { height: 35.5px; }
  .lunch-left { left: 94px; width: 340px; }
  .lunch-left .item { justify-content: flex-start; }
  .lunch-left .item-name { width: 222px; }
  .lunch-right { left: 469px; width: 314px; }
  .footer-note {
    position: absolute; left: 0; width: 849px; top: 1160px; text-align: center;
    font-family: "Arimo", Arial, sans-serif; font-weight: 400; font-size: 13px; color: var(--ink);
  }
</style>
</head>
<body>
<main class="menu-page">
  <div class="brand"><span class="brand-mark"></span><span class="brand-name">Corner Cup</span></div>
  <div class="menu-word">menu</div>

  <section class="section-box breakfast-box" aria-label="Breakfast"></section>
  <div class="banner banner-breakfast">
    <svg width="195" height="44" viewBox="0 0 195 44">
      <polygon points="1,3 194,3 184,22 194,41 1,41 11,22" fill="#000" stroke="#f5d45a" stroke-width="1.5"/>
    </svg>
    <span class="banner-label">BREAKFAST</span>
  </div>
  <ul class="item-list breakfast-list">
    <li class="item"><span class="item-name">Toast</span><span class="price">$2 per slice</span></li>
    <li class="item"><span class="item-name">Raisin Toast</span><span class="price">$2 per slice</span></li>
    <li class="item"><span class="item-name">Egg Bacon and Cheese Roll</span><span class="price">$6.5</span></li>
    <li class="item"><span class="item-name">Veggie Brekky Wrap</span><span class="price">$6.5</span></li>
    <li class="item"><span class="item-name">Ham and Cheese French Toast</span><span class="price">$6.5</span></li>
    <li class="item"><span class="item-name">Ham and Cheese Toastie</span><span class="price">$5.5</span></li>
    <li class="item"><span class="item-name">Cheese and Tomato Toastie</span><span class="price">$5.5</span></li>
    <li class="item"><span class="item-name">Ham and Cheese Croissant</span><span class="price">$6.5</span></li>
    <li class="item"><span class="item-name">Cheese and tomato Croissant</span><span class="price">$6.0</span></li>
    <li class="item"><span class="item-name">Ham Cheese and Tomato Toastie</span><span class="price">$6.0</span></li>
    <li class="item"><span class="item-name">Plain Croissant</span><span class="price">$3.5</span></li>
  </ul>

  <section class="section-box light-box" aria-label="Something light"></section>
  <div class="banner banner-light">
    <svg width="198" height="44" viewBox="0 0 198 44">
      <polygon points="1,3 197,3 187,22 197,41 1,41 11,22" fill="#000" stroke="#f5d45a" stroke-width="1.5"/>
    </svg>
    <span class="banner-label">SOMETHING LIGHT</span>
  </div>
  <ul class="item-list light-list">
    <li class="item"><span class="item-name">Mixed Yoghurts</span><span class="price">$5.5</span></li>
    <li class="item"><span class="item-name">Granola and Fruit Yoghurt</span><span class="price">$5.5</span></li>
    <li class="item"><span class="item-name">Chia Pudding</span><span class="price">$5.5</span></li>
    <li class="item"><span class="item-name">Bircher Muesli</span><span class="price">$5.5</span></li>
    <li class="item"><span class="item-name">Fruit Salad</span><span class="price">$5.5</span></li>
    <li class="item"><span class="item-name">Banana Bread</span><span class="price">$4.5</span></li>
    <li class="item"><span class="item-name">Muffins – made fresh daily</span><span class="price">$4.5</span></li>
    <li class="item"><span class="item-name">Slices</span><span class="price">$4.0</span></li>
    <li class="item"><span class="item-name">Cookies</span><span class="price">$4.0</span></li>
    <li class="item"><span class="item-name">Choc Crunch Energy Bite</span><span class="price">$4.0</span></li>
    <li class="item"><span class="item-name">Super Crunch Energy Bite</span><span class="price">$4.0</span></li>
    <li class="item"><span class="item-name">Chocolate Bar</span><span class="price">$3.0</span></li>
    <li class="item"><span class="item-name">Packet of Chips</span><span class="price">$3.0</span></li>
  </ul>

  <section class="section-box lunch-box" aria-label="Lunch"></section>
  <div class="banner banner-lunch">
    <svg width="186" height="44" viewBox="0 0 186 44">
      <polygon points="1,3 170,3 185,41 1,41 11,22" fill="#000" stroke="#f5d45a" stroke-width="1.5"/>
    </svg>
    <span class="banner-label">LUNCH</span>
  </div>
  <ul class="item-list lunch-list lunch-left">
    <li class="item"><span class="item-name">Pre made Sandwiches</span><span class="price">$6.5/$7.5</span></li>
    <li class="item"><span class="item-name">Pre made Focaccias</span><span class="price">$8.5</span></li>
    <li class="item"><span class="item-name">Pre made Wraps</span><span class="price">$7.5</span></li>
    <li class="item"><span class="item-name">Pre made Mini Rolls</span><span class="price">$4.0</span></li>
    <li class="item"><span class="item-name">Pre made Baguettes</span><span class="price">$9.0</span></li>
    <li class="item"><span class="item-name">Pre made Bagels</span><span class="price">$9.0</span></li>
  </ul>
  <ul class="item-list lunch-list lunch-right">
    <li class="item"><span class="item-name">Fresh Salads made daily</span><span class="price">$9.5</span></li>
    <li class="item"><span class="item-name">Hot Chips</span><span class="price">$4.5</span></li>
    <li class="item"><span class="item-name">Plain Hamburger</span><span class="price">$7.5</span></li>
    <li class="item"><span class="item-name">Hamburger with the Lot</span><span class="price">$9.0</span></li>
    <li class="item"><span class="item-name">Chicken Schnitzel Burger</span><span class="price">$8.5</span></li>
  </ul>

  <p class="footer-note">Visit us at addrerss goes here, contact and other information to be added.</p>
</main>
</body>
</html>
```